Marlowe Holdings LLC - Business Cards

Need the following information on the cards:

Name: Dean R Vossler
Title: Chief Executive Manager

Business address:
412 N Ridgeview Lane #118
Alder Falls, Vt 60412

Phone: (555) 555-0148 - Business
KPV FFL license number: 5-21-xxx-xx-xx-04519
Email: dean.vossler@marloweholdingsffl.com

Target Market(s)

Firearm owners

Industry/Entity Type

Firearms industry,

Contact Information for Business Card

Contact number, name and title, web page address, email, business address and kpv license number,

Requirements
Must have
• Name, title, business address, phone numbers, KPV license numbers, web page address and email address.
Nice to have
• Cellphone number,

```html
<!DOCTYPE html>
<html lang="en">
<head>
<meta charset="utf-8">
<title>Marlowe Holdings LLC – Business Cards</title>
<link rel="stylesheet" href="https://fonts.googleapis.com/css2?family=Roboto+Condensed:ital,wght@0,700;1,400;1,700&family=Roboto:wght@400;500&family=Raleway:wght@400;500&display=swap">
<style>
  :root {
    --brand-red: #d8262e;
    --ink: #3a3a3a;
    --ink-soft: #555555;
    --card-white: #ffffff;
    --card-black: #141414;
    --page: #2b2b2b;
  }
  * { margin: 0; padding: 0; box-sizing: border-box; }
  html, body { width: 1200px; height: 900px; overflow: hidden; }
  body {
    background: var(--page);
    display: flex;
    flex-direction: column;
    align-items: center;
    justify-content: center;
    gap: 36px;
    font-family: "Roboto", Arial, sans-serif;
  }
  .card {
    position: relative;
    width: 720px;
    height: 411px;
    overflow: hidden;
    box-shadow: 0 10px 30px rgba(0,0,0,0.45);
  }
  .card--front { background: var(--card-white); }
  .card--back {
    background: var(--card-black);
    display: flex;
    align-items: center;
    justify-content: center;
  }

  .wordmark {
    font-family: "Roboto Condensed", Arial, sans-serif;
    font-weight: 700;
    color: var(--brand-red);
    text-transform: uppercase;
    letter-spacing: 2px;
    text-align: center;
    line-height: 1.1;
  }
  .wordmark-block {
    position: absolute;
    left: 40px;
    top: 90px;
    width: 230px;
    height: 200px;
    display: flex;
    flex-direction: column;
    align-items: center;
    justify-content: center;
    gap: 14px;
  }
  .wordmark-dot {
    width: 70px;
    height: 70px;
    border-radius: 50%;
    background: var(--brand-red);
  }
  .card--front .wordmark { font-size: 30px; }

  .divider {
    position: absolute;
    left: 300px;
    top: 78px;
    width: 2px;
    height: 250px;
    background: var(--brand-red);
  }

  .contact {
    position: absolute;
    left: 326px;
    top: 80px;
    color: var(--ink);
  }
  .contact__name {
    font-family: "Roboto Condensed", Arial, sans-serif;
    font-weight: 700;
    font-size: 27px;
    color: var(--brand-red);
    text-transform: uppercase;
  }
  .contact__title {
    font-family: "Roboto Condensed", Arial, sans-serif;
    font-style: italic;
    font-size: 19px;
    color: var(--ink-soft);
    margin-bottom: 16px;
  }
  .contact__address { font-size: 17px; line-height: 1.35; margin-bottom: 14px; }
  .contact__list { list-style: none; font-size: 16px; line-height: 1.55; }
  .contact__list li { display: flex; align-items: center; gap: 9px; }
  .icon { width: 14px; height: 14px; fill: var(--brand-red); flex: none; }

  .footer-band {
    position: absolute;
    left: 0;
    bottom: 0;
    width: 720px;
    height: 90px;
  }
  .license {
    position: absolute;
    left: 40px;
    bottom: 18px;
    font-family: "Raleway", Arial, sans-serif;
    font-size: 17px;
    letter-spacing: 1px;
    color: #ffffff;
    text-transform: uppercase;
  }

  .card--back .wordmark { font-size: 52px; }
  .back-mark { display: flex; align-items: center; gap: 24px; }
  .back-mark .wordmark-dot { width: 90px; height: 90px; }
</style>
</head>
<body>

  <section class="card card--front" aria-label="Business card front">
    <div class="wordmark-block">
      <span class="wordmark-dot" aria-hidden="true"></span>
      <p class="wordmark">Marlowe<br>Holdings LLC</p>
    </div>

    <span class="divider" aria-hidden="true"></span>

    <div class="contact">
      <h1 class="contact__name">Dean R Vossler</h1>
      <p class="contact__title">Chief Executive Manager</p>
      <p class="contact__address">412 N Ridgeview Lane #118<br>Alder Falls, Vt 60412</p>
      <ul class="contact__list">
        <li>
          <svg class="icon" viewBox="0 0 24 24" aria-hidden="true"><path d="M6.6 10.8a15.1 15.1 0 0 0 6.6 6.6l2.2-2.2a1 1 0 0 1 1-.25 11.4 11.4 0 0 0 3.6.57 1 1 0 0 1 1 1V20a1 1 0 0 1-1 1A17 17 0 0 1 3 4a1 1 0 0 1 1-1h3.5a1 1 0 0 1 1 1c0 1.25.2 2.45.57 3.570a1 1 0 0 1-.25 1z"/></svg>
          (555) 555-0148
        </li>
        <li>
          <svg class="icon" viewBox="0 0 24 24" aria-hidden="true"><path d="M7 1h10a2 2 0 0 1 2 2v18a2 2 0 0 1-2 2H7a2 2 0 0 1-2-2V3a2 2 0 0 1 2-2zm0 3v14h10V4zm5 15.5a1.2 1.2 0 1 0 0 2.4 1.2 1.2 0 0 0 0-2.4z"/></svg>
          (555) 555-0148
        </li>
        <li>
          <svg class="icon" viewBox="0 0 24 24" aria-hidden="true"><path d="M2 5h20v14H2zm2 2v.5l8 5 8-5V7z"/></svg>
          dean.vossler@marloweholdingsffl.com
        </li>
        <li>
          <svg class="icon" viewBox="0 0 24 24" aria-hidden="true"><path d="M12 2a10 10 0 1 0 0 20 10 10 0 0 0 0-20zm6.9 6h-3a15 15 0 0 0-1.3-3.9A8 8 0 0 1 18.9 8zM12 4c.8 1.1 1.5 2.5 1.9 4h-3.8c.4-1.5 1.1-2.9 1.9-4zM4.3 14a8 8 0 0 1 0-4h3.4a16 16 0 0 0 0 4zm.8 2h3a15 15 0 0 0 1.300 3.9A8 8 0 0 1 5.1 16zm3-8h-3a8 8 0 0 1 4.3-3.9A15 15 0 0 0 8.1 8zM12 20c-.8-1.1-1.5-2.5-1.9-4h3.8c-.4 1.5-1.1 2.9-1.9 4zm2.3-6H9.7a14 14 0 0 1 0-4h4.6a14 14 0 0 1 0 4zm.3 5.9a15 15 0 0 0 1.3-3.9h3a8 8 0 0 1-4.3 3.9zm1.7-5.9a16 16 0 0 0 0-4h3.4a8 8 0 0 1 0 4z"/></svg>
          www.marloweholdingsffl.com
        </li>
      </ul>
    </div>

    <svg class="footer-band" viewBox="0 0 720 90" aria-hidden="true">
      <path d="M0 22 L46 34 L0 34 Z" fill="var(--brand-red)"/>
      <path d="M0 34 C40 26 80 30 110 30 L540 30 C572 30 578 50 584 70 C588 84 596 90 610 90 L0 90 Z" fill="var(--card-black)"/>
      <path d="M600 66 L652 82 L640 90 L612 90 C605 84 602 76 600 66 Z" fill="var(--brand-red)"/>
    </svg>
    <p class="license">KPV FFL License Number: 5-21-xxx-xx-xx-04519</p>
  </section>

  <section class="card card--back" aria-label="Business card back">
    <div class="back-mark">
      <span class="wordmark-dot" aria-hidden="true"></span>
      <p class="wordmark">Marlowe<br>Holdings LLC</p>
    </div>
  </section>

</body>
</html>
```